BrightNest

Need a 6 page template designed in Layered PSD for a house cleaning company.

Target Market(s)

People who are selling their homes and need house cleaning

Industry/Entity Type

House cleaning

Number of Pages Required

5+ page

Font styles to use
Sans Serif

Requirements
Must have
• Please see the zip file included with the brief. It has a document with detailed instructions.

```html
<!DOCTYPE html>
<html lang="en">
<head>
<meta charset="utf-8">
<title>BrightNest – Deep Cleaning</title>
<link rel="stylesheet" href="https://fonts.googleapis.com/css2?family=Fira+Sans+Condensed:ital,wght@1,400;1,500&family=Roboto:wght@400;500;700&display=swap">
<style>
:root{
  --navy:#1c2f7f;
  --navy-deep:#15246a;
  --green:#4fae2f;
  --green-light:#62c23c;
  --text:#4a4a4a;
  --muted:#666;
  --grey-bg:#f0f1f3;
  --white:#fff;
}
*{box-sizing:border-box;margin:0;padding:0}
html,body{width:1200px;height:5249px;overflow:hidden}
body{font-family:"Roboto",sans-serif;color:var(--text);background:var(--white);position:relative}
.abs{position:absolute}
.heading{font-family:"Fira Sans Condensed",sans-serif;font-style:italic;font-weight:400;color:var(--navy);line-height:1.22}
.rule{width:86px;height:4px;background:var(--green);border-radius:2px}
.btn{display:inline-block;background:var(--green);color:var(--white);font-weight:700;font-size:13px;text-transform:uppercase;letter-spacing:.3px;padding:0 26px;height:46px;line-height:46px;border-radius:12px 4px 12px 4px}
p{font-size:14px;line-height:1.85}

/* header */
.site-header{left:0;top:0;width:1200px;height:137px;background:var(--white)}
.brand{display:flex;align-items:center;gap:10px;font-family:"Roboto",sans-serif;font-weight:700;font-size:34px;color:var(--navy)}
.brand-dot{width:18px;height:18px;border-radius:50%;background:var(--green)}
.site-header .brand{position:absolute;left:112px;top:46px}
.main-nav{position:absolute;left:391px;top:60px;display:flex;gap:30px;font-size:14px;font-weight:700;color:#222;text-transform:uppercase}
.main-nav .active{color:var(--navy)}
.site-header .btn{position:absolute;left:941px;top:49px;height:45px;line-height:45px;padding:0 28px}

/* hero */
.hero{left:0;top:137px;width:1200px;height:700px;overflow:hidden}
.hero-photo{position:absolute;inset:0;background:linear-gradient(110deg,#1a2a72 0%,#233a8e 45%,#2a4598 70%,#1b2d78 100%)}
.hero .heading{position:absolute;left:112px;top:118px;width:460px;color:var(--white);font-size:35px}
.hero .rule{position:absolute;left:112px;top:300px;width:72px}
.hero .lead{position:absolute;left:112px;top:326px;width:470px;color:var(--white);font-size:17px;line-height:1.7}
.hero .btn{position:absolute;left:112px;top:437px}
.hero svg{position:absolute;left:0;bottom:0}

/* pre-sale */
.round-photo{border-radius:50%;border:7px solid var(--navy)}
.presale-photo{left:112px;top:845px;width:436px;height:436px;background:radial-gradient(circle at 50% 45%,#d8b08a,#a5764e 55%,#7b5636)}
.presale-title{left:599px;top:848px;width:480px;font-size:35px}
.presale-rule{left:599px;top:993px}
.presale-text{left:599px;top:1030px;width:490px;text-align:justify}
.presale-btn{left:599px;top:1222px}

/* services */
.services-title{left:0;top:1380px;width:1200px;text-align:center;font-size:35px}
.services-rule{left:557px;top:1433px}
.tiles{left:0;top:1489px;width:1200px;height:361px;display:flex}
.tile{flex:1;position:relative;border-radius:14px 0 14px 0;overflow:hidden}
.tile.blue{background:linear-gradient(160deg,#2b3f95,#1a2a75)}
.tile.green{background:linear-gradient(160deg,#5cbf35,#3f9a22)}
.tile span{position:absolute;left:0;right:0;top:296px;text-align:center;color:var(--white);font-weight:700;font-size:18px;text-transform:uppercase}

/* move-in */
.movein-title{left:150px;top:1946px;width:900px;text-align:center;font-size:33px}
.movein-text{left:150px;top:2073px;width:900px;text-align:center;font-size:13.5px}

/* realtors */
.realtor-title{left:112px;top:2260px;font-size:37px}
.realtor-rule{left:112px;top:2318px}
.realtor-text{left:112px;top:2340px;width:428px;text-align:justify;font-size:14px}
.realtor-btn{left:112px;top:2599px}
.realtor-frame{left:591px;top:2532px;width:168px;height:166px;border:3px solid var(--green)}
.realtor-photo{left:625px;top:2253px;width:429px;height:411px;background:linear-gradient(135deg,#e9edf2,#cfd8e2 60%,#b7c3d1)}

/* move-out */
.moveout{left:0;top:2813px;width:1200px;height:855px;background:linear-gradient(180deg,#54b52f,#46a226)}
.moveout-title{left:300px;top:2882px;width:600px;text-align:center;font-size:35px;color:var(--white)}
.moveout-text{left:150px;top:3004px;width:900px;text-align:center;color:var(--white);font-size:13.5px;font-weight:400}
.cards{left:112px;top:3143px;width:976px;display:flex;gap:26px}
.card{width:308px;height:448px;background:var(--white);border-radius:4px;padding:30px 22px 0;text-align:center;box-shadow:0 6px 18px rgba(0,0,0,.12)}
.card-icon{width:90px;height:90px;border-radius:50%;margin:0 auto 22px;display:flex;align-items:center;justify-content:center}
.card-icon.navy{background:var(--navy)}
.card-icon.green{background:var(--green)}
.card h3{font-size:16px;font-weight:700;color:#222;text-transform:uppercase;line-height:1.5;margin-bottom:24px}
.card p{font-size:12px;line-height:1.9;color:var(--muted)}

/* about */
.about{left:0;top:3668px;width:1200px;height:589px;background:var(--grey-bg)}
.about-photo{left:112px;top:3744px;width:434px;height:434px;background:radial-gradient(circle at 50% 50%,#eceae6,#d2ccc4 55%,#b3a99c)}
.about-title{left:599px;top:3780px;width:460px;font-size:35px}
.about-rule{left:599px;top:3960px}
.about-text{left:599px;top:3982px;width:490px;text-align:justify;font-size:14px}

/* areas */
.areas-title{left:112px;top:4345px;font-size:37px}
.areas-rule{left:112px;top:4402px}
.area-list{list-style:none;font-size:17px;color:#222;line-height:27.4px}
.area-list li::before{content:"•";margin-right:22px;color:#333}
.area-a{left:112px;top:4438px}
.area-b{left:310px;top:4438px}
.map{left:591px;top:4380px;width:500px;height:266px;background:linear-gradient(160deg,#b9bcc2,#9a9ea6);border-radius:30px 60px 40px 80px}

/* footer */
.footer{left:0;top:4680px;width:1200px;height:569px}
.footer svg{position:absolute;left:0;top:0}
.footer-body{position:absolute;left:0;top:170px;width:1200px;height:399px;background:var(--navy)}
.f-col{position:absolute;top:262px;color:var(--white)}
.f-col h4{font-size:15px;font-weight:700;text-transform:uppercase;margin-bottom:22px}
.f-links{list-style:none;font-size:14px;line-height:39px}
.f-links li{display:flex;align-items:center;gap:18px}
.f-bullet{width:12px;height:12px;border-radius:50%;border:3px solid var(--green)}
.f-item{display:flex;gap:20px;margin-bottom:20px;font-size:12px;line-height:1.7}
.f-item b{display:block;font-size:13px;text-transform:uppercase}
.f-icon{width:12px;height:12px;margin-top:3px;flex:none}
.footer .brand{position:absolute;left:560px;top:324px;color:var(--white);font-size:36px}
.socials{position:absolute;left:603px;top:404px;display:flex;gap:10px}
.socials span{width:33px;height:33px;border-radius:50%;background:var(--white)}
.socials span:first-child{background:var(--green)}
.copyright{position:absolute;left:0;top:528px;width:1200px;text-align:center;color:var(--white);font-size:12px}
</style>
</head>
<body>

<header class="site-header abs">
  <div class="brand"><span class="brand-dot"></span>BrightNest</div>
  <nav class="main-nav">
    <span class="active">Home</span><span>Services</span><span>What's Included</span><span>For Realtors</span><span>Blog</span>
  </nav>
  <span class="btn">Contact Us</span>
</header>

<section class="hero abs">
  <div class="hero-photo" role="img" aria-label="Tidy living room photo under a deep blue overlay"></div>
  <h1 class="heading">The Only Barrie Area Cleaning Service That Specializes in Deep Pre-Sale, Move-In, &amp; Move-Out House Cleanings</h1>
  <div class="rule"></div>
  <p class="lead">Welcome to the only Barrie area cleaning service specializing in deep move-in, move-out, and pre-sale house cleanings.</p>
  <span class="btn">Learn More</span>
  <svg width="1200" height="240" viewBox="0 0 1200 240" aria-hidden="true">
    <path d="M0 120 C260 230 520 200 760 130 C930 80 1080 70 1200 110 L1200 240 L0 240 Z" fill="#fff"/>
    <path d="M0 120 C260 230 520 200 760 130 C930 80 1080 70 1200 110 L1200 160 C1100 110 960 110 800 150 C560 210 300 220 0 140 Z" fill="#4fae2f"/>
    <path d="M600 200 C800 150 1000 120 1200 150 L1200 175 C1020 140 830 160 640 205 Z" fill="#4fae2f"/>
  </svg>
</section>

<div class="abs round-photo presale-photo" role="img" aria-label="Couple sitting among moving boxes looking at a tablet"></div>
<h2 class="abs heading presale-title">Pre-Sale Cleanings: Are You Putting Your Barrie Area Home Up for Sale?</h2>
<div class="abs rule presale-rule"></div>
<p class="abs presale-text">First impressions matter, and a clean and fresh home can make a huge difference. At BrightNest.com, we specialize in deep cleaning services that will get your home in tip-top shape for potential buyers. Not only will a move-out deep cleaning make your home more attractive to potential buyers, but it can also increase its value. A well-maintained home is a valuable asset that can command a higher price on the Barrie area market.</p>
<span class="abs btn presale-btn">Read More</span>

<h2 class="abs heading services-title">Cleaning Services We Offer</h2>
<div class="abs rule services-rule"></div>
<div class="abs tiles">
  <div class="tile blue" role="img" aria-label="Cleaner wiping a surface, blue tint"><span>Pre-Sale Cleaning</span></div>
  <div class="tile green" role="img" aria-label="Gloved hand cleaning a table, green tint"><span>Move-In Cleaning</span></div>
  <div class="tile blue" role="img" aria-label="Cleaner in an empty room, blue tint"><span>Move-Out Cleaning</span></div>
  <div class="tile green" role="img" aria-label="Cleaning supplies on a counter, green tint"><span>Junk Removal</span></div>
</div>

<h2 class="abs heading movein-title">Move-In Cleanings: Take the Stress Out of Your Move &amp; Have Your Home Sparkling Clean Before You Move In</h2>
<p class="abs movein-text">Moving doesn't have to be a stressful experience. Let us take the hassle out of your move and ensure your new Barrie home is clean, fresh, and ready for you to settle in. Our Barrie area move-in deep cleaning Service is designed so that you can start your new chapter with a spotless and hygienic environment. Our experienced and skilled cleaners will work diligently to ensure that every nook and cranny of your new Barrie home is perfectly cleaned.</p>

<h2 class="abs heading realtor-title">Attention Realtors</h2>
<div class="abs rule realtor-rule"></div>
<div class="abs realtor-text">
  <p>As a Barrie area realtor, you know that buying or selling a home can be stressful for your clients. Here at BrightNest.com, we want to help make that process as smooth as possible. That's why we're excited to introduce our Barrie area move-in &amp; move-out deep cleaning services as a value-added service for your clients.</p>
  <p style="margin-top:10px">Let us take the hassle out of your client's move and ensure their Barrie home is deep-cleaned, fresh, and ready.</p>
</div>
<span class="abs btn realtor-btn">Click Here For More Info</span>
<div class="abs realtor-frame"></div>
<div class="abs realtor-photo" role="img" aria-label="Cleaner in a mask holding spray bottles and giving a thumbs up"></div>

<section class="abs moveout" role="img" aria-label="Green-tinted photo of a clean kitchen"></section>
<h2 class="abs heading moveout-title">Move-Out Cleanings: Cleaned &amp; Ready for The Next Occupants</h2>
<p class="abs moveout-text">Looking for a professional move-out cleaning service to ensure that your property is left sparkling clean and ready for the next occupants? Look no further than our expert team of cleaning professionals! At BrightNest.com, we provide move-out cleaning services to homeowners and tenants throughout the Barrie area. Our team of experienced and fully trained cleaners will work tirelessly to ensure your property is left in pristine condition when you move out so that you can focus on your move without any added stress.</p>
<div class="abs cards">
  <article class="card">
    <div class="card-icon navy"><svg width="44" height="40" viewBox="0 0 44 40" fill="none" stroke="#fff" stroke-width="2.2" aria-hidden="true"><path d="M6 20 L22 6 L38 20"/><path d="M11 16 V34 H33 V16"/><path d="M18 34 V24 H26 V34"/></svg></div>
    <h3>Move-Out Cleaning<br>For Homeowners</h3>
    <p>Move-out cleaning for Barrie area homeowners is a deep cleaning service typically performed when the homeowner prepares to move out. The purpose of move-out cleaning is to leave the property in a sparkling clean condition, ready for the next occupants to move in or for the final inspection by the new homeowner.</p>
  </article>
  <article class="card">
    <div class="card-icon green"><svg width="44" height="40" viewBox="0 0 44 40" fill="none" stroke="#fff" stroke-width="2.2" aria-hidden="true"><path d="M6 18 L22 5 L38 18"/><rect x="11" y="18" width="22" height="16"/><path d="M22 18 V34 M11 26 H33"/></svg></div>
    <h3>Move-Out Cleaning<br>For Renters</h3>
    <p>Are you moving out of your Barrie area rental property soon and need to ensure that the property is left clean and in pristine condition to get your security deposit back? Don't let the stress of move-out cleaning get in the way of getting your security deposit back. Contact us today to schedule your move-out cleaning service, and let us help you enjoy a smooth transition when you move out.</p>
  </article>
  <article class="card">
    <div class="card-icon navy"><svg width="44" height="40" viewBox="0 0 44 40" fill="none" stroke="#fff" stroke-width="2.2" aria-hidden="true"><path d="M30 4 L18 24"/><path d="M12 22 L24 28 L20 36 L6 36 Z"/><path d="M34 14 l2 2 m0 -4 l-2 2 M38 24 l2 0"/></svg></div>
    <h3>Move Out Cleaning For<br>Landlords &amp; Property</h3>
    <p>Move-out cleaning for Barrie area landlords &amp; property managers is a deep cleaning service typically performed when a tenant vacates the rental property. This deep cleaning is critical in ensuring that rental properties are in good condition, ready for new tenants, and preventing any delays in the turnover process.</p>
  </article>
</div>

<section class="abs about"></section>
<div class="abs round-photo about-photo" role="img" aria-label="Two cleaners in pink gloves tidying a kitchen"></div>
<h2 class="abs heading about-title">The Only Barrie Area Cleaning Service That Specializes in Deep Pre-Sale, Move-In &amp; Move-Out House Cleanings</h2>
<div class="abs rule about-rule"></div>
<p class="abs about-text">Whether you're moving into or out of a Barrie area home, apartment, or rental property, our Barrie area Pre-Sale, Move-In, and Move-Out Deep Cleaning Services are the perfect solution for you. Contact us today to schedule an appointment, and let us take care of the daunting task of having your home deep cleaned so that you can enjoy your new Barrie area home from day one.</p>

<h2 class="abs heading areas-title">Areas We Service</h2>
<div class="abs rule areas-rule"></div>
<ul class="abs area-list area-a">
  <li>Barrie</li><li>Innisfil</li><li>Springwater</li><li>Minesing</li><li>Orillia</li><li>Wasaga</li><li>Midland</li><li>Angus</li><li>Collingwood</li>
</ul>
<ul class="abs area-list area-b">
  <li>New Lowell</li><li>Oro-Medonte</li><li>Shanty Bay</li><li>Horseshoe Valley</li><li>Coldwater</li><li>Stayner</li><li>Creemore</li><li>Alliston</li><li>And everywhere in between</li>
</ul>
<div class="abs map" role="img" aria-label="Grey map with navy location pins marking service areas"></div>

<footer class="abs footer">
  <svg width="1200" height="200" viewBox="0 0 1200 200" aria-hidden="true">
    <path d="M0 20 C200 120 500 150 800 150 C1000 150 1120 150 1200 170 L1200 200 L0 200 Z" fill="#1c2f7f"/>
    <path d="M0 10 C220 110 520 140 820 140 C1000 140 1120 140 1200 160 L1200 172 C1100 150 980 152 800 152 C500 152 200 122 0 30 Z" fill="#4fae2f"/>
    <path d="M0 40 C150 110 300 140 480 150 C300 150 150 130 0 70 Z" fill="#4fae2f"/>
  </svg>
  <div class="footer-body"></div>

  <div class="f-col" style="left:112px">
    <h4>Quick Links</h4>
    <ul class="f-links">
      <li><span class="f-bullet"></span>Home</li>
      <li><span class="f-bullet"></span>Services</li>
      <li><span class="f-bullet"></span>What's Included</li>
      <li><span class="f-bullet"></span>For Realtors</li>
      <li><span class="f-bullet"></span>Blog</li>
    </ul>
  </div>

  <div class="f-col" style="left:326px;width:200px">
    <h4>Contact Info</h4>
    <div class="f-item"><svg class="f-icon" viewBox="0 0 12 12" aria-hidden="true"><path d="M6 0a4 4 0 0 1 4 4c0 3-4 8-4 8S2 7 2 4a4 4 0 0 1 4-4z" fill="#4fae2f"/></svg><div><b>Address:</b>212 Harbour Lane,<br>Barrie, ON</div></div>
    <div class="f-item"><svg class="f-icon" viewBox="0 0 12 12" aria-hidden="true"><path d="M2 0h3l1 3-2 1a7 7 0 0 0 4 4l1-2 3 1v3a1 1 0 0 1-1 1A11 11 0 0 1 1 1a1 1 0 0 1 1-1z" fill="#4fae2f"/></svg><div><b>Phone:</b>+1 (555) 014 2290</div></div>
    <div class="f-item"><svg class="f-icon" viewBox="0 0 12 12" aria-hidden="true"><path d="M0 2h12v8H0z" fill="#4fae2f"/><path d="M0 2l6 5 6-5" stroke="#1c2f7f" fill="none"/></svg><div><b>Email:</b>info@brightnest.ca</div></div>
  </div>

  <div class="brand"><span class="brand-dot"></span>BrightNest</div>
  <div class="socials" aria-label="Social links"><span></span><span></span><span></span><span></span></div>

  <div class="f-col" style="left:851px;width:260px">
    <h4>Availability</h4>
    <div class="f-item"><svg class="f-icon" viewBox="0 0 12 12" aria-hidden="true"><circle cx="6" cy="6" r="5" stroke="#4fae2f" stroke-width="1.6" fill="none"/><path d="M6 3v3l2 1" stroke="#4fae2f" stroke-width="1.4" fill="none"/></svg><div><b>Opening Hours:</b>Open 7 Days a Week (Monday-Sunday)<br>Hours 8:00 am – 9:00 pm<br>Evenings &amp; Weekends (Yes)<br>Short Notice (Yes)</div></div>
  </div>

  <div class="copyright">© 2023 BRIGHTNEST &nbsp;|&nbsp; All Rights Reserved</div>
</footer>

</body>
</html>
```